Best in class cloud software provider for retailers needs a new business card design to reflect prod

We are a software company based out of Chicago selling into retailers. We have a new website and marketing collateral that support our new product designs. We are obsessed with simplicity, ease of use, and having a really powerful product set. We have two products as noted on our website - www.plumvector.example - one is a retail task management product and the other is a Help Ticketing product.

At PlumVector we are passionate about creating the best Retail Task Management system in the industry. We bring more than 20 years of retail operations, Workforce Management and Retail Task experience and have a set of web and mobile software features that no one else has. PlumVector enables you to plan and distribute work throughout your organization and ensure it gets done.

We need a new business card design that reflects our new branding, message and approach.

I've attached a few documents that help support what we are building and how our colors look.

There may be additional future work if this goes well.

Thanks,
Brian

President

Target Market(s)

We sell into retailers and are a software company

Industry/Entity Type

Software

Contact Information for Business Card

The card must have

Name
title
address
tele
email
PlumVector logo (someplace)

So for example

It would have for me

Brian Okafor
President
47 North Garnet Ave. Suite 310
Chicago, IL 60618
3127814063
bokafor@plumvector.example

Requirements
Must have
• We need to cards for 5 different people - same design different names etc
Nice to have
• should reflect our colors and product and website - be creative - ease of use, simplicity, and power is what the product is about - but we are very forward PlumVector and hear all the time that our product is gorgeous. The font should be consistent with our website, and marketing one pager included
Should not have
• Strange or unfamiliar colors or fonts...

```html
<!DOCTYPE html>
<html lang="en">
<head>
<meta charset="utf-8">
<title>PlumVector Business Card</title>
<link href="https://fonts.googleapis.com/css2?family=Almendra:wght@700&family=Open+Sans:wght@400;600&display=swap" rel="stylesheet">
<style>
  :root {
    --brand-orange: #f26b2a;
    --card-black: #000000;
    --card-white: #ffffff;
    --stage: #dcdcdc;
    --divider: #5a5a5a;
  }
  * { margin: 0; padding: 0; box-sizing: border-box; }
  html, body {
    width: 1189px; height: 1200px; overflow: hidden;
    background: var(--stage);
  }
  .canvas { position: relative; width: 1189px; height: 1200px; }
  .card {
    position: absolute; left: 140px; width: 917px; height: 523px;
    overflow: hidden; box-shadow: 0 6px 14px rgba(0,0,0,0.35);
  }
  .card--front { top: 46px; background: var(--card-white); }
  .card--back { top: 600px; background: var(--card-black); }
  .front-shape { position: absolute; inset: 0; }
  .wordmark {
    position: absolute; left: 0; right: 0; text-align: center;
    font-family: "Open Sans", sans-serif; font-weight: 600;
    color: var(--brand-orange); letter-spacing: -2px; line-height: 1;
  }
  .card--front .wordmark { top: 86px; font-size: 128px; }
  .card--back .wordmark { top: 210px; font-size: 134px; }
  .person {
    position: absolute; right: 554px; top: 352px; text-align: right;
    color: var(--card-white);
  }
  .person__name {
    font-family: "Almendra", serif; font-weight: 700; font-size: 38px; line-height: 1;
  }
  .person__title {
    font-family: "Open Sans", sans-serif; font-size: 23px; line-height: 1.2;
    margin-top: 4px; letter-spacing: 0.5px;
  }
  .divider {
    position: absolute; left: 404px; top: 328px; width: 1px; height: 138px;
    background: var(--divider);
  }
  .contact {
    position: absolute; left: 440px; top: 338px; list-style: none;
    font-family: "Open Sans", sans-serif; font-size: 21px; color: var(--card-white);
    line-height: 26px;
  }
  .contact__item { display: flex; align-items: flex-start; margin-bottom: 9px; }
  .contact__icon { width: 16px; height: 16px; margin-top: 5px; margin-right: 20px; flex: none; }
</style>
</head>
<body>
<div class="canvas">
  <section class="card card--front">
    <svg class="front-shape" viewBox="0 0 917 523" width="917" height="523" aria-hidden="true">
      <path d="M0,173 Q458,437 917,173 L917,523 L0,523 Z" fill="var(--card-black)"/>
      <path d="M31,187 Q458,410 872,195 Q458,380 31,187 Z" fill="var(--brand-orange)"/>
    </svg>
    <div class="wordmark">PlumVector</div>
    <div class="person">
      <div class="person__name">Brian Okafor</div>
      <div class="person__title">President</div>
    </div>
    <div class="divider"></div>
    <ul class="contact">
      <li class="contact__item">
        <svg class="contact__icon" viewBox="0 0 16 16" aria-hidden="true">
          <rect width="16" height="16" fill="var(--brand-orange)"/>
          <path d="M3,6 Q8,2 13,6 L11,7 L10,6 L6,6 L5,7 Z M4,8 L12,8 L12,13 L4,13 Z" fill="var(--card-black)"/>
        </svg>
        <span>3127814063</span>
      </li>
      <li class="contact__item">
        <svg class="contact__icon" viewBox="0 0 16 16" aria-hidden="true">
          <rect width="16" height="16" fill="var(--brand-orange)"/>
          <rect x="3" y="4.5" width="10" height="7" fill="none" stroke="var(--card-black)" stroke-width="1.3"/>
          <path d="M3,4.5 L8,8.5 L13,4.5" fill="none" stroke="var(--card-black)" stroke-width="1.3"/>
        </svg>
        <span>bokafor@plumvector.example</span>
      </li>
      <li class="contact__item">
        <svg class="contact__icon" viewBox="0 0 16 16" aria-hidden="true">
          <rect width="16" height="16" fill="var(--brand-orange)"/>
          <path d="M8,13 L4.8,7.5 A3.6,3.6 0 1 1 11.2,7.5 Z" fill="var(--card-black)"/>
          <circle cx="8" cy="6" r="1.3" fill="var(--brand-orange)"/>
        </svg>
        <span>47 North Garnet Ave. Suite 310<br>Chicago, IL 60618</span>
      </li>
    </ul>
  </section>
  <section class="card card--back">
    <div class="wordmark">PlumVector</div>
  </section>
</div>
</body>
</html>
```